Morvell Electric Business Card

An electrical contractor needs a business card design, that will stand out.
I would like designs that use the colors in the logo shown. The logo attached I am ok with but if you have a better idea I am open for suggestions. I like the color scheme.
Industry/Entity Type
Electrical
Contact Information for Business Card
Services, social media, QR code,

```html
<!DOCTYPE html>
<html lang="en">
<head>
<meta charset="utf-8">
<title>Morvell Electric Business Card</title>
<link href="https://fonts.googleapis.com/css2?family=Montserrat:wght@500;600&family=Open+Sans:wght@400;600&display=swap" rel="stylesheet">
<style>
  :root {
    --canvas: #8a8a8a;
    --card-dark: #262626;
    --brand-yellow: #f4b400;
    --ink-dark: #1e1e1e;
    --ink-light: #f2f2f2;
  }
  * { margin: 0; padding: 0; box-sizing: border-box; }
  html, body { width: 1200px; height: 900px; overflow: hidden; }
  body {
    background: var(--canvas);
    position: relative;
    font-family: "Open Sans", sans-serif;
  }
  .card {
    position: absolute;
    left: 250px;
    width: 700px;
    height: 400px;
    border-radius: 20px;
    overflow: hidden;
    background: var(--card-dark);
  }
  .card--front { top: 40px; }
  .card--back { top: 460px; }
  .card__bands { position: absolute; inset: 0; }

  .brand {
    position: absolute;
    display: flex;
    align-items: center;
    gap: 18px;
    color: var(--ink-light);
    font-family: "Montserrat", sans-serif;
    font-weight: 600;
    letter-spacing: 1px;
    text-transform: uppercase;
    white-space: nowrap;
  }
  .brand__square {
    background: var(--brand-yellow);
    border-radius: 10px;
  }
  .card--front .brand { left: 0; right: 0; top: 130px; justify-content: center; font-size: 42px; }
  .card--front .brand__square { width: 54px; height: 54px; }

  .website {
    position: absolute;
    left: 250px; right: 0;
    top: 345px;
    text-align: center;
    color: var(--ink-dark);
    font-weight: 600;
    font-size: 17px;
    letter-spacing: 7px;
  }

  .person {
    position: absolute;
    left: 34px; top: 18px;
    padding-left: 12px;
    border-left: 3px solid var(--ink-dark);
    color: var(--ink-dark);
  }
  .person__name { font-family: "Montserrat", sans-serif; font-weight: 500; font-size: 24px; line-height: 1.1; }
  .person__role { font-size: 13px; }

  .contact {
    position: absolute;
    left: 34px; top: 130px;
    font-size: 14px;
    line-height: 1.6;
  }
  .contact__address { color: var(--brand-yellow); font-weight: 600; margin-bottom: 6px; }
  .contact__row { display: flex; align-items: center; gap: 10px; color: var(--ink-light); }
  .contact__icon { width: 18px; height: 18px; }

  .card--back .brand { right: 40px; bottom: 60px; font-size: 30px; }
  .card--back .brand__square { width: 44px; height: 44px; }
</style>
</head>
<body>

<section class="card card--front">
  <svg class="card__bands" viewBox="0 0 700 400" aria-hidden="true">
    <path fill="var(--brand-yellow)" d="M0,372 L170,372 C205,372 210,318 250,318 L700,318 L700,400 L0,400 Z"/>
  </svg>
  <div class="brand"><span class="brand__square"></span>Morvell Electric</div>
  <p class="website">www.morvellelectric.com</p>
</section>

<section class="card card--back">
  <svg class="card__bands" viewBox="0 0 700 400" aria-hidden="true">
    <path fill="var(--brand-yellow)" d="M0,0 L700,0 L700,28 L420,28 C380,28 372,88 330,88 L0,88 Z"/>
  </svg>
  <div class="person">
    <p class="person__name">Corra Delmont</p>
    <p class="person__role">Director</p>
  </div>
  <div class="contact">
    <p class="contact__address">2250 Ashcroft Lane Suite 310,<br>Dalewood Tx 70412</p>
    <p class="contact__row">
      <svg class="contact__icon" viewBox="0 0 18 18" aria-hidden="true">
        <circle cx="9" cy="9" r="9" fill="var(--brand-yellow)"/>
        <path d="M6 4.5 L7.6 4.5 L8.2 7 L7.2 7.8 C7.8 9.2 8.8 10.2 10.2 10.8 L11 9.8 L13.5 10.4 L13.5 12 C13.5 12.8 12.8 13.5 12 13.5 C8.4 13.3 4.7 9.6 4.5 6 C4.5 5.2 5.2 4.5 6 4.5 Z" fill="var(--ink-dark)"/>
      </svg>
      555-014-2278
    </p>
    <p class="contact__row">
      <svg class="contact__icon" viewBox="0 0 18 18" aria-hidden="true">
        <circle cx="9" cy="9" r="9" fill="var(--brand-yellow)"/>
        <rect x="4.5" y="6" width="9" height="6.5" rx="1" fill="var(--ink-dark)"/>
        <path d="M4.8 6.4 L9 9.6 L13.2 6.4" stroke="var(--brand-yellow)" stroke-width="1" fill="none"/>
      </svg>
      corra@morvellmail.com
    </p>
  </div>
  <div class="brand"><span class="brand__square"></span>Morvell Electric</div>
</section>

</body>
</html>
```